Infographic for council approvals process

Looking to show the different steps that a person needs to undertake to get local council approval for their new swimming pool. It's a bit convoluted and text heavy when written out, but could be more graphically illustrated as a series of steps and choices.
Needs to be aligned to the brand for www.LagoonBuildPacksOnline.com.au

Target Market(s)

Home Owners

Font styles to use
Sans Serif

Requirements
Must have
• Nice graphics that help simplify and layout the process graphically, the infographic should reference our brand colours and logos.

```html
<!DOCTYPE html>
<html lang="en">
<head>
<meta charset="utf-8">
<title>Lagoon Build Packs Online – Pool Approval Guide</title>
<link href="https://fonts.googleapis.com/css2?family=Barlow:wght@400;500;600;700&family=Barlow+Semi+Condensed:wght@600;700;800&display=swap" rel="stylesheet">
<style>
:root{
  --navy:#12344d;
  --yellow:#f6c932;
  --teal:#5fc5ca;
  --tint:#e9f5f5;
  --tint-soft:#f3fafa;
  --rule:#c9d3d8;
  --ink:#1d2a33;
  --white:#ffffff;
}
*{margin:0;padding:0;box-sizing:border-box}
html,body{width:1200px;height:3590px;overflow:hidden;background:var(--white)}
body{position:relative;font-family:"Barlow",sans-serif;color:var(--ink)}
.abs{position:absolute}
.connectors{position:absolute;left:0;top:0;width:1200px;height:3590px}
.placeholder{position:absolute;border-radius:10px}

/* brand */
.brand{left:0;top:80px;width:1200px;display:flex;justify-content:center;align-items:center}
.brand-name{font-family:"Barlow",sans-serif;font-weight:700;font-size:38px;line-height:40px;color:var(--navy);letter-spacing:.5px;text-align:left}

/* headings */
.band{position:absolute;background:var(--navy);color:var(--white);font-family:"Barlow Semi Condensed",sans-serif;font-weight:700;display:flex;align-items:center;white-space:nowrap}
.band em{font-style:normal;color:var(--yellow)}
.band-title{left:132px;top:212px;width:948px;height:60px;font-size:42px;padding-left:16px}
.band-nsw{left:290px;top:576px;width:602px;height:51px;font-size:34px;justify-content:center;font-weight:600}
.band-docs{height:34px;font-size:24px;padding-left:10px}
.band-cdc{left:86px;top:1057px;width:433px}
.band-da{left:676px;top:1057px;width:425px;padding-left:22px}
.band-after{left:365px;top:1638px;width:795px;height:52px;font-size:36px;padding-left:38px}
.band-guide{left:185px;top:1966px;width:840px;height:51px;justify-content:center;font-size:38px;font-weight:800;color:var(--yellow)}
.band-tips{left:325px;top:2813px;width:829px;height:52px;font-size:33px;padding-left:14px}
.side-line{position:absolute;height:3px;background:var(--teal)}

.panel{position:absolute;background:linear-gradient(90deg,var(--tint) 0%,var(--tint-soft) 100%)}
.body-text{font-size:19px;line-height:29px}

.option-bar{position:absolute;height:30px;background:var(--yellow);color:var(--navy);font-family:"Barlow Semi Condensed",sans-serif;font-weight:600;font-size:22px;display:flex;align-items:center;justify-content:center}
.option-text{position:absolute;font-size:16px;line-height:26px;text-align:center}

/* document lists */
.doc-list{position:absolute;list-style:none;counter-reset:doc}
.doc-list li{counter-increment:doc;position:relative;padding-left:44px;font-size:14.5px;line-height:20px;margin-bottom:9px}
.doc-list li::before{content:counter(doc);position:absolute;left:14px;top:0;width:20px;height:20px;border-radius:50%;background:var(--navy);color:var(--white);font-size:12px;font-weight:700;display:flex;align-items:center;justify-content:center}
.doc-note{position:absolute;font-size:14.5px;line-height:20px;font-weight:700;color:var(--navy)}

/* table */
.guide-table{position:absolute;left:184px;top:2035px;width:836px;border-collapse:collapse;table-layout:fixed}
.guide-table td{font-size:15px;line-height:22px;padding:6px 4px;vertical-align:top;border-bottom:1px solid var(--rule)}
.guide-table td.label{width:254px;background:linear-gradient(90deg,var(--tint),var(--tint-soft));color:var(--navy);border-bottom:1px solid var(--white)}
.guide-table td.value{padding-left:32px}
.guide-table tr.short td.value{border-bottom:none;background:linear-gradient(var(--rule),var(--rule)) left bottom/425px 1px no-repeat}
.guide-table tr:last-child td{border-bottom:none}

/* tips */
.tip{position:absolute;display:flex;gap:10px;font-size:19.5px;line-height:27px}
.tip-num{flex:0 0 28px;background:var(--navy);color:var(--white);display:flex;align-items:center;justify-content:center;font-size:18px}
</style>
</head>
<body>

<svg class="connectors" viewBox="0 0 1200 3590" aria-hidden="true">
  <g fill="none" stroke="#12344d" stroke-width="4">
    <path d="M290 602 H164 V792 H186"/>
    <path d="M892 602 H1032 V792 H1010"/>
    <path d="M560 788 H574 V1073 H532"/>
    <path d="M634 792 H620 V1073 H664"/>
  </g>
  <g fill="#12344d">
    <polygon points="184,781 198,792 184,803"/>
    <polygon points="1012,781 998,792 1012,803"/>
    <polygon points="534,1062 519,1073 534,1084"/>
    <polygon points="662,1062 677,1073 662,1084"/>
  </g>
</svg>

<header class="abs brand">
  <span class="brand-name">LAGOON BUILD<br>PACKS ONLINE</span>
</header>

<div class="side-line" style="left:0;top:234px;width:132px"></div>
<div class="side-line" style="left:0;top:245px;width:132px"></div>
<div class="side-line" style="left:1080px;top:234px;width:120px"></div>
<div class="side-line" style="left:1080px;top:245px;width:120px"></div>
<h1 class="band band-title">What do I need to do to get my&nbsp;<em>POOL APPROVED?</em></h1>

<div class="placeholder" role="img" aria-label="Illustration of a hand signing a clipboard checklist" style="left:84px;top:300px;width:264px;height:251px;background:linear-gradient(160deg,#d9eef0,#9fd6da)"></div>
<div class="panel" style="left:376px;top:293px;width:704px;height:234px"></div>
<p class="abs body-text" style="left:389px;top:300px;width:685px">Navigating the planning requirements for installing a swimming pool can be a complex process, varying significantly across different Australian states. In New South Wales (NSW), Queensland (QLD), Victoria (VIC), and the Australian Capital Territory (ACT), understanding the specific regulations and procedures is crucial for a successful project. Each state has its own approval process, required permits, compliance standards, and inspection procedures.</p>

<h2 class="band band-nsw"><em>COUNCIL APPROVAL</em>&nbsp;for a Pool in NSW</h2>
<div class="panel" style="left:206px;top:630px;width:770px;height:109px;background:linear-gradient(180deg,var(--tint),var(--white))"></div>
<p class="abs" style="left:240px;top:638px;width:702px;font-size:17px;line-height:25px;text-align:center">In NSW, every new pool construction must receive approval from a Licensed Certifier. Depending on the specific circumstances, some pools may need a Complying Development (CDC), while others will need a Development Application (DA) approval from the council.</p>

<div class="option-bar" style="left:195px;top:778px;width:365px">Option 1: CDC</div>
<p class="option-text" style="left:202px;top:829px;width:356px">Most customers prefer to apply for a CDC as it is a faster, cheaper and straight forward process with a private certifier instead of the local council. In order to apply for a CDC, certain criteria need to be met. Make sure you look at this criteria to ensure you are eligible.</p>

<div class="option-bar" style="left:634px;top:778px;width:366px">Option 2: DA</div>
<p class="option-text" style="left:638px;top:829px;width:362px">If you don't meet the requirements for a CDC, you'll need to obtain development consent from your local Council by submitting a Development Application (DA). This is the sole approval pathway in certain scenarios, such as if you're building a new home. Unfortunately this is a longer and more expensive process so make sure you get this underway as soon as possible.</p>

<h3 class="band band-docs band-cdc">What documents do I need for a&nbsp;<em>CDC</em>?</h3>
<div class="panel" style="left:118px;top:1094px;width:398px;height:456px"></div>
<ol class="doc-list" style="left:122px;top:1104px;width:386px">
  <li>CDC Application form</li>
  <li>Section 10.7 Certificate for the Site Address. You can purchase this from your local Council and it will tell you if you are eligible for a CDC. This 10.7 Certificate will also notify you if your site is designated as a floodplain, heritage site, slope hazard zone, or acid sulphate soil risk area. This is important as you will need to consult with specific professionals for the approvals if any of these are identified.</li>
  <li>Deposited Plan/88b. This will check if there are any easements around the proposed site.</li>
  <li>Architectural Plans from an architect or a draftsperson</li>
  <li>Local Water Authority Endorsement</li>
  <li>Pool Engineering Drawings</li>
  <li>BASIX Certificate (Building Sustainability Index. This is only required if your pool is over 40,000L capacity</li>
</ol>
<p class="doc-note" style="left:128px;top:1488px;width:385px">Additional documents may be requested such as an arborist report, bushfire attack level or a flood certificate depending on your site.</p>

<h3 class="band band-docs band-da">Documents for a&nbsp;<em>DA approval</em></h3>
<div class="panel" style="left:676px;top:1094px;width:397px;height:300px;background:linear-gradient(180deg,var(--tint),var(--white))"></div>
<ol class="doc-list" style="left:680px;top:1104px;width:388px">
  <li>Statement of Environmental Effect (SEE)</li>
  <li>Site Survey/Plan</li>
  <li>Detailed DA Design Drawings. These should be completed by an architect or draftsperson and include a number of requirements, check with your local Council for what they require.</li>
  <li>Structural Engineers Pool Drawings and Certification</li>
  <li>Builders Home Warranty Insurance</li>
  <li>Copy of payment receipt for Long Service Levy</li>
  <li>Water Authority Tap In Approval</li>
</ol>
<div class="placeholder" role="img" aria-label="Illustration of a ticked checklist clipboard between potted plants" style="left:725px;top:1394px;width:237px;height:223px;border-radius:50% 50% 10px 10px;background:linear-gradient(180deg,#a9dfe2,#e3f4f4)"></div>

<div class="placeholder" role="img" aria-label="Illustration of workers installing a swimming pool beside an umbrella and sun lounger" style="left:49px;top:1631px;width:300px;height:244px;background:linear-gradient(160deg,#dff1f3,#5ab9ea)"></div>
<h2 class="band band-after">What happens after my&nbsp;<em>POOL IS INSTALLED?</em></h2>
<div class="panel" style="left:383px;top:1690px;width:777px;height:185px"></div>
<p class="abs body-text" style="left:404px;top:1700px;width:700px;line-height:26.5px">When you're fibreglass pool and pool fence is installed, you'll be ready for a pool inspection. This is the last stage of the pool approval journey. An inspector will visit the site and ensure all regulations have been met. The inspector will conduct inspections, measurements, tests, and capture photographs of your pool gates, pool fences, dividing fences utilised as pool fences, and any objects or structures in close proximity to the pool fence.</p>

<div class="side-line" style="left:0;top:1986px;width:185px"></div>
<div class="side-line" style="left:0;top:1996px;width:185px"></div>
<div class="side-line" style="left:1025px;top:1986px;width:175px"></div>
<div class="side-line" style="left:1025px;top:1996px;width:175px"></div>
<h2 class="band band-guide">DESIGN GUIDELINES</h2>

<table class="guide-table">
  <tr class="short"><td class="label">Legislation</td><td class="value">AS1926.1-2012 (Modified)</td></tr>
  <tr class="short"><td class="label">Relocatable Definition</td><td class="value">No definitions apply.</td></tr>
  <tr class="short"><td class="label">Exemptions from Approval</td><td class="value">Volume &lt;2000L w. lockable lid.</td></tr>
  <tr class="short"><td class="label">Boundary fence as barrier</td><td class="value">YES. 1800mm high.</td></tr>
  <tr class="short"><td class="label">Boundary offset: Above Ground</td><td class="value">1.0m MIN. to waterline. Coping may encroach.<br>**Pools (structures over 1400mm high require DA)</td></tr>
  <tr class="short"><td class="label">Boundary offset: Inground</td><td class="value">1.0m MIN. to waterline. Coping may encroach</td></tr>
  <tr><td class="label">Pool Wass as Barrier</td><td class="value">No</td></tr>
  <tr><td class="label">Build on Easements</td><td class="value">NO under CDC (Barrier ok) May be considered under DA- Council specific.</td></tr>
  <tr><td class="label">Support Slabs</td><td class="value">Support Slabs</td></tr>
  <tr><td class="label">CPR Signs (add note on plans)</td><td class="value">YES, mandatory. Must be displayed in the immediate vicinity of the pool area and<br>read from a distance of 3m.</td></tr>
  <tr><td class="label">Safety Barriers</td><td class="value">AS1926.1-2012 Standard modified: Can not use pool wall. Lockable lid,<br>spas only up to 4.0m long. All other NCZ's as per AS1926.1-2012 (Vic).</td></tr>
  <tr><td class="label">Body of Water as Barrier</td><td class="value">NO</td></tr>
  <tr><td class="label">Lockable Lids</td><td class="value">YES, seated spas only. Not acceptable on swim spas where a person can move around.<br>&lt;2000 L w. lid. No permit req'd.<br>&gt;2000 L. Lid accepted but permit req'd (lid specs req'd, must be capable<br>of being operated by 1 person)</td></tr>
  <tr><td class="label">Vegetation Near Barriers</td><td class="value">Outside NCZ's.</td></tr>
  <tr><td class="label">Doors &amp; Windows</td><td class="value">No doors. Any windows/openings fixed to 100mm MAX. opening.</td></tr>
  <tr><td class="label">Pool Equipment</td><td class="value">Outside NCZ's</td></tr>
</table>
<div class="placeholder" role="img" aria-label="Illustration of a businessman in a suit holding a briefcase" style="left:850px;top:2035px;width:140px;height:230px;background:linear-gradient(180deg,#e8f3f4,#9fd3d7)"></div>

<div class="placeholder" role="img" aria-label="Illustration of three professionals discussing plans" style="left:42px;top:2767px;width:272px;height:251px;background:linear-gradient(160deg,#e4f3f3,#7fc8cc)"></div>
<h2 class="band band-tips">Tips for Successfully Navigating&nbsp;<em>Planning Requirements</em></h2>
<div class="panel" style="left:325px;top:2865px;width:829px;height:170px"></div>
<div class="panel" style="left:80px;top:3020px;width:1074px;height:360px"></div>

<div class="tip" style="left:328px;top:2890px;width:820px">
  <span class="tip-num">1</span>
  <p>Thoroughly research and understand local regulations. Take the time to familiarise yourself with the specific planning requirements in your area to ensure compliance. It's always best to have a clear roadmap a the beginning of what is required. A checklist is a great way to track the process.</p>
</div>
<div class="tip" style="left:80px;top:3032px;width:1070px">
  <span class="tip-num">2</span>
  <p>Seek professional guidance when needed. If you encounter complexities or uncertainties in the planning process, don't hesitate to consult with professionals. There are aspects of the approval process that can be quite daunting, especially if your site has certain additional regulation requirements due to soil type or flood plain issues. Sometimes it's best to use a professional service that can take care of the approval process for you.</p>
</div>
<div class="tip" style="left:80px;top:3164px;width:1070px">
  <span class="tip-num">3</span>
  <p>Complete all necessary paperwork accurately and on time. Ensure that you submit all required documentation promptly and accurately, as delays or errors in paperwork can prolong the approval process.</p>
</div>
<div class="tip" style="left:80px;top:3241px;width:1070px">
  <span class="tip-num">4</span>
  <p>Stay informed about any updates or changes to regulations. The regulations can change so keep in touch with your local Council to ensure your application is up to date with the latest standards.</p>
</div>

<div class="placeholder" role="img" aria-label="Illustration of pool water with a ladder at the edge" style="left:0;top:3436px;width:1200px;height:154px;border-radius:0;background:linear-gradient(180deg,#5ec3dc 0%,#2f9fc8 100%)"></div>

</body>
</html>
```